Full 10+ Page Online Learning eBook Design - NOT just the cover :)

We currently have an eBook within the online learning space which is geared towards a consumer audience (hobbyists, interests), but we have a new 2.0 version which is geared towards professionals (certifications, training, continuing ed, career-oriented). We need a new design and need the words/copy put into the eBook, but want to keep the look and feel of the original (open to variations in design). File is attached, along with various logo options.

Target Market(s)

Professionals

Industry/Entity Type

Learning

Font styles to use
Sans Serif

Colors
33a6d7
acd036
919191

Requirements
Must have
• Must follow a very similar look a feel of the original file. We use a lot of fonts like Raleway, Gotham, Helvetica Neue, Gil Sans, DIN - anything modern looking. We also use a lot of grayish hexagons in our corporate design. Feel free to check out brightmeadowlabs.example to get a better sense.
Nice to have
• Include some professionally oriented icons / photos
Should not have
• No cartoonish graphics or imagery

```html
<!DOCTYPE html>
<html lang="en">
<head>
<meta charset="utf-8">
<title>Monetization Options</title>
<link href="https://fonts.googleapis.com/css2?family=Didact+Gothic&family=Lato:wght@400&display=swap" rel="stylesheet">
<style>
  :root {
    --brand-blue: #33a6d7;
    --box-blue: #2fa3d6;
    --band-gray: #8e8e8e;
    --ink: #111111;
    --paper: #ffffff;
  }
  * { margin: 0; padding: 0; box-sizing: border-box; }
  html, body { width: 852px; height: 1200px; overflow: hidden; background: var(--paper); }
  .page {
    position: relative;
    width: 852px;
    height: 1200px;
    font-family: "Didact Gothic", sans-serif;
    color: var(--ink);
  }
  .hero-photo {
    position: absolute;
    left: 0; top: 0;
    width: 852px; height: 372px;
    background:
      radial-gradient(ellipse 120px 60px at 50% 62%, rgba(90,200,220,0.45), transparent 70%),
      radial-gradient(ellipse 260px 70px at 48% 40%, rgba(220,60,70,0.35), transparent 70%),
      radial-gradient(ellipse 300px 90px at 70% 30%, rgba(240,170,80,0.25), transparent 70%),
      linear-gradient(180deg, #1b1e28 0%, #2a2630 35%, #1d2a30 60%, #0d0f12 100%);
  }
  .options {
    position: absolute;
    left: 10px; top: 400px;
    width: 505px;
  }
  .options-title {
    font-size: 20px;
    font-weight: 400;
    letter-spacing: 0.3px;
    padding-bottom: 4px;
    border-bottom: 2px solid var(--brand-blue);
    margin-bottom: 12px;
  }
  .options p {
    font-size: 13.6px;
    line-height: 17.9px;
  }
  .options .intro { width: 470px; }
  .licensing {
    position: absolute;
    left: 516px; top: 402px;
    width: 328px; height: 622px;
    background: var(--box-blue);
    color: var(--paper);
  }
  .licensing-title {
    font-size: 17px;
    font-weight: 400;
    padding: 2px 6px 3px;
    border-bottom: 2px solid var(--paper);
    margin-bottom: 12px;
  }
  .licensing p {
    font-size: 13.6px;
    line-height: 17.8px;
    padding: 0 8px 0 6px;
  }
  .case-study {
    position: absolute;
    left: 6px; top: 1056px;
    width: 840px; height: 130px;
    background: var(--band-gray);
    color: var(--paper);
    font-family: "Lato", sans-serif;
    font-size: 14.4px;
    line-height: 18.4px;
    text-align: center;
    padding: 10px 14px 0;
  }
</style>
</head>
<body>
<div class="page">
  <div class="hero-photo" role="img" aria-label="Night photograph of a wet city street at road level with blurred red, blue and amber lights"></div>

  <section class="options">
    <h2 class="options-title">MONETIZATION OPTIONS</h2>
    <p class="intro">As you build a business case to turn your content into paid learning, consider several forms of monetization. Each of these monetization options can be deployed singly or stacked with others, as long as your technology platform for ecommerce and distribution can accommodate the variations.</p>
    <p>B2P Learning:Business-to-consumer (B2C) and business-to-business (B2B) publishing have long been understood. Business-to-professional or B2P is a newer phenomenon, selected and paid for by individuals to stay on the top of their professions. They provide a credit card directly and you sell them a digital product. In this business model, the transaction is with an end user.The product they're purchasing may be served up in ala carte form (one set of lessons) or it may be sold as a continuing annual subscription, giving the customer access to digital courses for a set period.</p>
    <p>Seat licensing: Whereas B2P targets the individual customer, this business model pursues the entire company that wants effectively trained employees. In this case, your organization has developed an entire catalog of content, which you license to other organizations for use in their corporate training.This business model has several variations. (See "Notes about Licensing" to learn more.)</p>
    <p>Sponsored Learning: This takes a couple of forms. The learning company creates content that's made available to the learner either through the funding provided by a sponsor or by serving up ads. For example, if your business focuses on generating content related to finance, you may develop a course using pre-existing content about a specific subject -- saving for retirement, funding a college education -- and have a financial services company sponsor it to make available to their clients and prospects. Similarly, the course may include advertising from one or more companies and fed to your prospects and theirs.</p>
    <p>Content Marketing: This business model emphasizes lead generation by making the learning content free in return for registration information to build your database.</p>
  </section>

  <aside class="licensing">
    <h3 class="licensing-title">Notes about Licensing</h3>
    <p>Seat licensing offers nuances worth exploring. The idea is to take your content and courses and license it to your largest customers or clients. Take, for example, a company that provides research and training services and delivers various certification programs to its primary user base in a B2P model. They may also go to their larger corporate customers with a compilation of content and courses and deliver those in one of three formats:</p>
    <p>Basic seat licensing: The corporate customer acquires a certain number of licenses and makes those available to employees, who take courses alongside others with similar professional interests but from different companies and may interact online with those individuals;</p>
    <p>Branded licensing: The corporate customer acquires a subscription with the stipulation that it's branded for their employees, who proceed to take courses only alongside other employees within the same organization; and</p>
    <p>Interoperability licensing:It may be that your clients already have a learning application they prefer to use. With the use of interoperability standards (SCORM being the most common one), they can pull in your content and run it on the course delivery platform of their choice.</p>
    <p>The overall idea is to give each corporate customer unique access and a branded experience.</p>
  </aside>

  <section class="case-study">
    <p>The Northfield Analytics Institute (NAI), a major division of Harborline Media, tapped its portfolio of content covering business intelligence, data analytics, data management and related topics to launch a new online learning center. The organization is delivering that new business line on the Bright Meadow Labs' Learning Business Platform, a cloud-based service chosen for its customizable front-end site creation, drag-and-drop course authoring, built-in e-commerce functionality and financial reporting. Now NAI is monetizing its training content through seat licensing to large corporations as well as individual data professionals with one-off and bundled sets of courses.</p>
  </section>
</div>
</body>
</html>
```